Brava Stone Oven Kitchen (restaurant)

Restaurant with a cool vibe.
We need a refresh of existing site. Appealing to a hip crowd of 25 or older age bracket (mid price to high small town). Constant changes food and cocktail menu. A vibing atmosphere with jazz funk hip music.
Must be able to scale for any device… phone/mobile device super important.
Instagram: @Brava.Linwell
Website: bravalinwell.example

Target Market(s)

25-55 age group

Number of Pages Required

1 page

Font styles to use
Sans Serif

Requirements
Must have
• Simple to navigate. Simplicity is the key to all sophistication.

Links/Buttons
Menu
Gift Cards
Reservations
Take Out
Contact Us
Should not have
• Please, nothing generic looking… no cookie cutter look. Originality

```html
<!DOCTYPE html>
<html lang="en">
<head>
<meta charset="utf-8">
<title>Brava Stone Oven Kitchen</title>
<link rel="stylesheet" href="https://fonts.googleapis.com/css2?family=Montserrat:wght@300;400;500;600;700;800&family=Oswald:wght@500;600&family=Roboto+Slab:wght@400;500&family=Open+Sans:wght@400;600&display=swap">
<style>
:root{
  --ink:#1c1c1c;
  --panel:#222222;
  --deep:#0b0b0b;
  --white:#ffffff;
  --muted:#b9b9b9;
  --red:#e0271a;
  --orange:#ff7a00;
  --grad:linear-gradient(90deg,#ff8a00,#e41b17);
  --gradv:linear-gradient(180deg,#ff8a00,#e41b17);
}
*{box-sizing:border-box;margin:0;padding:0}
html,body{width:1200px;height:4222px;overflow:hidden;background:var(--deep)}
body{position:relative;font-family:"Montserrat",sans-serif;color:var(--white)}
section,header,footer{position:absolute;left:0;width:1200px}
.abs{position:absolute}
.center{text-align:center}
.btn{position:absolute;display:flex;align-items:center;justify-content:center;background:var(--grad);border-radius:30px;color:#fff;font:700 13px "Montserrat",sans-serif;letter-spacing:.5px;text-transform:uppercase;text-decoration:none}
.eyebrow{font:500 15px "Roboto Slab",serif;letter-spacing:2px;color:var(--red);text-transform:uppercase}
.title{font:300 36px "Montserrat",sans-serif;text-transform:uppercase;letter-spacing:.5px}
.title b{font-weight:700}
.copy{font:400 13px/25px "Open Sans",sans-serif;color:var(--muted)}
.photo{position:absolute}
.frame{position:absolute;border:2px solid rgba(255,255,255,.55)}
.frame-inner{position:absolute;border:1px solid rgba(255,255,255,.25)}

/* header / hero */
.hero{top:0;height:680px}
.hero .photo{inset:0;background:linear-gradient(180deg,#3a2420 0%,#7a3b2c 35%,#5a2d24 60%,#2a2a2e 100%)}
.hero .shade{position:absolute;inset:0;background:rgba(0,0,0,.35)}
.nav a{position:absolute;top:36px;font:600 12px "Montserrat",sans-serif;color:#fff;text-decoration:none;text-transform:uppercase}
.nav .active::after{content:"";position:absolute;left:-6px;right:-6px;top:22px;height:2px;background:var(--red)}
.brand{position:absolute;text-align:center;font:800 34px/1 "Montserrat",sans-serif;letter-spacing:2px}
.brand small{display:block;font:500 12px "Montserrat",sans-serif;letter-spacing:.3px;margin-top:3px}
.hero-box{left:257px;top:233px;width:682px;height:150px;border:2px solid rgba(255,255,255,.6)}
.hero-kicker{top:258px;width:1200px;font:500 24px "Montserrat",sans-serif;letter-spacing:3px}
.hero-title{top:290px;width:1200px;font:800 52px "Montserrat",sans-serif;letter-spacing:2px}
.arrow{position:absolute;top:300px}

/* welcome */
.welcome{top:611px;height:463px;left:103px;width:992px;background:var(--panel);box-shadow:0 0 30px rgba(0,0,0,.6);z-index:3}
.ring{position:absolute;left:67px;top:45px;width:374px;height:374px;border-radius:50%;background:linear-gradient(160deg,#ff8a00,#e41b17);padding:18px}
.ring .photo{position:static;width:100%;height:100%;border-radius:50%;border:6px solid #111;background:radial-gradient(circle at 45% 40%,#e08a3a,#7a3a24 55%,#2f3a26)}

/* menu */
.menu-band{top:1005px;height:511px}
.menu-band .photo{inset:0;background:radial-gradient(ellipse at 50% 50%,#4a4a4a,#1a1a1a 75%)}
.menu-intro{position:absolute;left:0;width:1200px}
.board{top:1431px;left:89px;width:1021px;height:498px;background:linear-gradient(180deg,#242424,#1b1b1b)}
.dish{position:absolute;text-align:center;z-index:2}
.dish .plate{position:absolute;border-radius:50%;border:4px solid #ddd}
.dish h3{font:600 16px "Oswald",sans-serif;text-transform:uppercase;letter-spacing:.5px;white-space:nowrap}
.dish p{width:140px;margin:6px auto 0;font:400 9px/14px "Open Sans",sans-serif;color:#8c8c8c}
.featured{position:absolute;left:482px;top:1705px;width:233px;height:164px;background:var(--gradv);border-radius:0 0 40px 40px;z-index:1}

/* gift cards */
.gifts{top:1987px;height:516px;background:#151515}
.voucher{position:absolute;top:2182px;width:485px;height:228px;background:#262626;border-radius:0 90px 90px 0}
.voucher .photo{left:0;top:0;width:250px;height:228px;border-radius:0 0 114px 0}
.badge{position:absolute;left:190px;top:70px;width:82px;height:82px;border-radius:50%;background:#111;border:4px solid var(--red);display:flex;flex-direction:column;align-items:center;justify-content:center;font:700 22px "Montserrat",sans-serif;line-height:1}
.badge small{font:600 8px "Montserrat",sans-serif;margin-top:3px}
.v-text{position:absolute;left:270px;width:200px;top:48px;text-align:center}
.v-text .kind{font:400 17px "Roboto Slab",serif;color:var(--red);text-transform:uppercase}
.v-text h4{font:700 30px "Montserrat",sans-serif;text-transform:uppercase;line-height:1}
.v-text .valid{font:700 10px "Montserrat",sans-serif;margin-top:10px}
.v-text p{font:400 9px/16px "Open Sans",sans-serif;color:#9a9a9a;margin-top:8px}

/* reservation */
.reserve{top:2503px;height:492px;background:#141414}
.reserve .photo{left:0;top:0;width:760px;height:492px;background:linear-gradient(90deg,#3a2a22 0%,#4a3a30 60%,#141414 100%)}

/* takeout */
.takeout{top:2995px;height:578px;background:#000}

/* contact */
.contact{top:3573px;height:381px;background:linear-gradient(90deg,#1b1b1b,#252525 50%,#1b1b1b)}
.info{position:absolute;top:3810px;width:280px;text-align:center;font:700 14px "Montserrat",sans-serif}
.info svg{display:block;margin:0 auto 12px}

/* footer */
.foot{top:3954px;height:268px;background:#000}
.foot-nav a{position:absolute;top:4082px;font:600 12px "Montserrat",sans-serif;color:#fff;text-decoration:none;text-transform:uppercase}
.social{position:absolute;top:4145px;width:32px;height:32px;border-radius:50%}
</style>
</head>
<body>

<header class="hero">
  <div class="photo" role="img" aria-label="Red brick restaurant building on a street corner with traffic lights"></div>
  <div class="shade"></div>
  <nav class="nav">
    <a class="active" href="#about" style="left:146px">About us</a>
    <a href="#menu" style="left:259px">Menu</a>
    <a href="#reservation" style="left:346px">Reservation</a>
    <a href="#takeout" style="left:780px">Takeout</a>
    <a href="#gift-cards" style="left:888px">Gift cards</a>
    <a href="#contact" style="left:1012px">Contact</a>
  </nav>
  <div class="brand" style="left:480px;top:26px;width:240px">BRAVA<small>Stone Oven Kitchen</small></div>
  <div class="abs hero-box"></div>
  <div class="abs center hero-kicker">WELCOME TO BRAVA</div>
  <div class="abs center hero-title">STONE OVEN KITCHEN</div>
  <a class="btn" href="#reservation" style="left:489px;top:364px;width:219px;height:46px;font-size:14px">Book reservation</a>
  <svg class="arrow" style="left:34px" width="22" height="36" viewBox="0 0 22 36"><path d="M18 3 4 18l14 15" fill="none" stroke="#fff" stroke-width="4"/></svg>
  <svg class="arrow" style="left:1140px" width="22" height="36" viewBox="0 0 22 36"><path d="M4 3l14 15L4 33" fill="none" stroke="#fff" stroke-width="4"/></svg>
</header>

<section class="menu-band" id="menu">
  <div class="photo" role="img" aria-label="Dimmed black and white close-up of plated food"></div>
  <div class="abs center eyebrow" style="top:150px;width:1200px">Taste</div>
  <div class="abs center title" style="top:172px;width:1200px;font-size:37px">Our <b>Menu</b></div>
  <p class="abs center" style="top:221px;left:280px;width:640px;font:400 18px/27px 'Open Sans',sans-serif">Sed ut perspiciatis unde omnis iste natus error sit avoluptatem accusantium doloremque laudantium, totam rem .aperiam.</p>
  <a class="btn" href="#menu" style="left:506px;top:302px;width:154px;height:38px;font-size:11px">View our menu</a>
</section>

<section class="welcome" id="about">
  <div class="frame-inner" style="inset:14px"></div>
  <div class="ring"><div class="photo" role="img" aria-label="Close-up of a grilled steak sandwich with greens"></div></div>
  <svg class="abs" style="left:687px;top:79px" width="18" height="18" viewBox="0 0 18 18"><path d="M2 2l14 14M16 2 2 16" stroke="#fff" stroke-width="2"/></svg>
  <div class="abs center title" style="left:460px;width:470px;top:102px;font-size:31px">Welcome to <b>Brava</b></div>
  <p class="abs center copy" style="left:470px;width:450px;top:150px">Sed ut perspiciatis unde omnis iste natus error sit voluptatem accusantium doloremque laudantium, totam rem .<br>aperiam, eaque ipsa quae ab illo inventore veritatis et quasi architecto beatae vitae dicta sunt explicabo. Nemo enim ipsam voluptatem quia voluptas sit aspernatur aut odit aut fugit, sed quia consequuntur magni dolores eos qui ratione voluptatem sequi nesciunt explicabo.</p>
  <a class="btn" href="#menu" style="left:617px;top:327px;width:156px;height:38px;font-size:11px">View our menu</a>
</section>

<section class="board">
  <div class="frame-inner" style="inset:16px"></div>
</section>
<div class="featured"></div>
<div class="dish" style="left:156px;top:1524px;width:167px">
  <div class="plate photo" role="img" aria-label="Stone oven pizza topped with greens" style="left:0;top:0;width:167px;height:167px;background:radial-gradient(#c55a2a,#6a4a2a)"></div>
  <h3 style="margin-top:198px">Wodd fired pizza</h3><p>Sed ut perspiciatis unde omnis iste Sed ut perspiciatis</p>
</div>
<div class="dish" style="left:312px;top:1524px;width:167px">
  <div class="plate photo" role="img" aria-label="Burger with avocado" style="left:0;top:0;width:167px;height:167px;background:radial-gradient(#a2703a,#4a5a2a)"></div>
  <h3 style="margin-top:198px">Special burger</h3><p>Sed ut perspiciatis unde omnis iste Sed ut perspiciatis</p>
</div>
<div class="dish" style="left:717px;top:1524px;width:167px">
  <div class="plate photo" role="img" aria-label="Plated mains and pasta" style="left:0;top:0;width:167px;height:167px;background:radial-gradient(#8a7a50,#3a3a2a)"></div>
  <h3 style="margin-top:200px">Mains &amp; pasta</h3><p>Sed ut perspiciatis unde omnis iste Sed ut perspiciatis</p>
</div>
<div class="dish" style="left:879px;top:1524px;width:167px">
  <div class="plate photo" role="img" aria-label="Special pizza with tomato toppings" style="left:0;top:0;width:167px;height:167px;background:radial-gradient(#d8503a,#8a2a1a)"></div>
  <h3 style="margin-top:200px">Special pizza</h3><p>Sed ut perspiciatis unde omnis iste Sed ut perspiciatis</p>
</div>
<div class="dish" style="left:476px;top:1488px;width:245px">
  <div class="plate photo" role="img" aria-label="Fried burger with greens" style="left:0;top:0;width:245px;height:245px;border-width:5px;background:radial-gradient(#d88a3a,#7a3a24 60%,#2f3a4a)"></div>
  <h3 style="margin-top:268px;font-size:26px">Fried burger</h3><p style="color:#fff;font-size:11px;line-height:16px;width:170px">Sed ut perspiciatis unde omnis iste Sed ut perspiciatis</p>
</div>

<section class="gifts" id="gift-cards">
  <div class="abs center eyebrow" style="top:61px;width:1200px;font-size:13px">Offer &amp; discounts</div>
  <div class="abs center title" style="top:80px;width:1200px;font-size:35px">Gift <b>Cards</b></div>
  <p class="abs center copy" style="top:126px;width:1200px">Sed ut perspiciatis unde omnis iste natus error sit avoluptatem accusantium</p>
  <div class="abs" style="left:568px;top:454px;width:26px;height:3px;background:#fff"></div>
  <div class="abs" style="left:607px;top:454px;width:26px;height:3px;background:var(--red)"></div>
</section>
<div class="voucher" style="left:110px">
  <div class="photo" role="img" aria-label="Bowls of dips seen from above" style="background:linear-gradient(135deg,#7a6a3a,#b8782a 50%,#4a4a3a)"></div>
  <div class="badge">35%<small>DISCOUNT</small></div>
  <div class="v-text"><div class="kind">Main meal</div><h4>Voucher</h4><div class="valid">VALID 20 AUG 2021</div><p>Sed ut perspiciatis unde omnis iste natus error sit avoluptatem accusantium</p></div>
</div>
<div class="voucher" style="left:611px">
  <div class="photo" role="img" aria-label="Fired pizza slices on a board" style="background:linear-gradient(135deg,#6a3a2a,#c8603a 50%,#8a5a3a)"></div>
  <div class="badge" style="border-color:var(--orange)">25%<small>DISCOUNT</small></div>
  <div class="v-text"><div class="kind">Fired pizza</div><h4>Voucher</h4><div class="valid">VALID 20 AUG 2021</div><p>Sed ut perspiciatis unde omnis iste natus error sit avoluptatem accusantium</p></div>
</div>

<section class="reserve" id="reservation">
  <div class="photo" role="img" aria-label="Restaurant owners posing together in front of the stone oven"></div>
  <div class="frame" style="left:656px;top:98px;width:459px;height:271px;border-color:rgba(255,255,255,.7)"></div>
  <div class="abs" style="left:680px;top:90px;width:410px;height:290px;background:#141414"></div>
  <div class="abs center eyebrow" style="left:656px;width:459px;top:157px">Enjoy your meal</div>
  <div class="abs center title" style="left:656px;width:459px;top:180px;font-size:36px">Book <b>Reservation</b></div>
  <p class="abs center" style="left:690px;width:390px;top:230px;font:400 15px/20px 'Open Sans',sans-serif;color:#ddd">Sed ut perspiciatis unde omnis iste natus error sit avoluptatem accusantium doloremque</p>
  <a class="btn" href="#reservation" style="left:804px;top:288px;width:154px;height:38px;font-size:11px">Book now</a>
</section>

<section class="takeout" id="takeout">
  <div class="abs center eyebrow" style="left:93px;width:400px;top:177px">Enjoy</div>
  <div class="abs center title" style="left:93px;width:400px;top:198px;font-size:36px">Take <b>Out</b></div>
  <p class="abs center copy" style="left:133px;width:320px;top:251px;font-size:12px;line-height:19px">Sed ut perspiciatis unde omnis iste natus error sit avoluptatem accusantium doloremque laudantium, totam remium doloremque</p>
  <a class="btn" href="#takeout" style="left:216px;top:328px;width:154px;height:38px;font-size:11px">Book now</a>
  <div class="frame" style="left:478px;top:155px;width:120px;height:240px;border-right:none"></div>
  <div class="photo" role="img" aria-label="Outdoor patio with red chairs and a painted mural" style="left:603px;top:75px;width:512px;height:395px;background:linear-gradient(160deg,#e06030,#5a7a9a 40%,#8a5a3a 80%);border-radius:0 40px 0 40px"></div>
  <div class="photo" role="img" aria-label="Plate of grilled chicken tacos with lime" style="left:505px;top:170px;width:293px;height:215px;background:linear-gradient(135deg,#c8a050,#6a7a30 50%,#b8603a);border-radius:20px 0 20px 0;border:4px solid #000"></div>
</section>

<section class="contact" id="contact">
  <div class="frame" style="left:208px;top:66px;width:795px;height:275px;border-color:rgba(255,255,255,.6)"></div>
  <div class="abs center eyebrow" style="top:82px;width:1200px;font-size:13px">Contact us</div>
  <div class="abs center title" style="top:102px;width:1200px;font-size:35px">Get in <b>Touch</b></div>
  <svg class="abs" style="left:593px;top:152px" width="14" height="14" viewBox="0 0 14 14"><path d="M1 1l12 12M13 1 1 13" stroke="#fff" stroke-width="1.6"/></svg>
</section>
<div class="info" style="left:226px">
  <svg width="20" height="20" viewBox="0 0 24 24"><path d="M5 3h4l2 5-3 2a12 12 0 0 0 6 6l2-3 5 2v4a2 2 0 0 1-2 2A18 18 0 0 1 3 5a2 2 0 0 1 2-2z" fill="none" stroke="#ff7a00" stroke-width="1.6"/></svg>
  Phone: 555-014-2290</div>
<div class="info" style="left:471px">
  <svg width="20" height="20" viewBox="0 0 24 24"><path d="M22 2 2 10l8 3 3 8z M10 13l12-11" fill="none" stroke="#ff7a00" stroke-width="1.6"/></svg>
  hello@bravalinwell.example</div>
<div class="info" style="left:727px">
  <svg width="20" height="20" viewBox="0 0 24 24"><path d="M12 22s7-7 7-12a7 7 0 0 0-14 0c0 5 7 12 7 12z" fill="none" stroke="#ff7a00" stroke-width="1.6"/><circle cx="12" cy="10" r="2.5" fill="none" stroke="#ff7a00" stroke-width="1.6"/></svg>
  1208 Mercer Ave, Linwell</div>

<footer class="foot">
  <div class="brand" style="left:480px;top:46px;width:240px">BRAVA<small>Stone Oven Kitchen</small></div>
</footer>
<nav class="foot-nav">
  <a href="#top" style="left:234px">Home</a>
  <a href="#about" style="left:323px">About us</a>
  <a href="#menu" style="left:440px">Menu</a>
  <a href="#reservation" style="left:528px">Reservation</a>
  <a href="#takeout" style="left:670px">Takeout</a>
  <a href="#gift-cards" style="left:780px">Gift cards</a>
  <a href="#contact" style="left:908px">Contact</a>
</nav>
<div class="abs center" style="top:4114px;width:1200px;font:400 11px 'Open Sans',sans-serif;color:#ccc">Copyright © 2021 Brava All Right Reserved</div>
<div class="social" style="left:547px;background:var(--red)" aria-label="Social link"></div>
<div class="social" style="left:585px;background:#fff" aria-label="Social link"></div>
<div class="social" style="left:623px;background:#fff" aria-label="Social link"></div>

</body>
</html>
```